Leadership training for women Business + Spirit

I need a flyer for a leadership training to hand out after I've been doing public speaking. I would also like to send it as a PDF. so maybe A4 is a good size. I will probably also need a brochure, with some more in depth information, but to start with I like to just give them something so they get inspired to contact me for more information. You can see more of my style on www.tallheron.se . Its a training that combines business with spirit, heart with intellect. We focus both on strict leadership skills such as Setting objectives aligned with strategy, assess performance and spiritual practices such as meditation, connecting with your unique essence. I like the deign to communicate business and professional together with warmth, life and joy. Colourful with style. Empowerment. The attached style guide does not have to be followed strictly but please use it in combination with my site www.tallheron.se I've the logo in many different sizes. I've added the smallest one below. Use any images that you think might fit, doesn't have to be from my website, it could be from your resources. I've added some other images here in the brief too, I have many more but can't attach all of it :-).
Women in leadership positions age 30 - 60
Leadership

```html
<!DOCTYPE html>
<html lang="sv">
<head>
<meta charset="utf-8">
<title>Tall Heron Ledarskap – flyer</title>
<link rel="stylesheet" href="https://fonts.googleapis.com/css2?family=Oswald:wght@500;600&family=Lato:wght@400;700&display=swap">
<style>
  :root {
    --navy: #1d3049;
    --orange: #ef7d00;
    --white: #ffffff;
    --ink: #111418;
    --backdrop: #e6e6e6;
    --photo-dark: #3b2d28;
    --photo-light: #a88f80;
  }
  * { box-sizing: border-box; margin: 0; padding: 0; }
  html, body { width: 1200px; height: 1200px; overflow: hidden; }
  body { background: var(--backdrop); font-family: "Lato", sans-serif; color: var(--ink); }

  .flyer {
    position: absolute; left: 186px; top: 20px;
    width: 828px; height: 1160px;
    background: var(--white); overflow: hidden;
  }
  .hero { position: absolute; left: 0; top: 0; width: 828px; height: 495px; }
  .hero-shape { position: absolute; inset: 0; }

  .headline {
    position: absolute; left: 39px; top: 50px; width: 770px;
    font-family: "Oswald", sans-serif; font-weight: 600;
    font-size: 26px; line-height: 29px; color: var(--white);
    text-transform: uppercase; letter-spacing: -0.3px;
  }
  .headline-rule { position: absolute; left: 43px; top: 121px; width: 495px; height: 4px; background: var(--orange); }

  .intro { position: absolute; left: 46px; top: 153px; width: 760px; color: var(--white); font-size: 14.6px; line-height: 19.5px; }
  .intro p { margin-bottom: 13px; }

  .focus-list { position: absolute; left: 40px; top: 282px; width: 720px; list-style: none; color: var(--white); font-size: 14.6px; line-height: 19.5px; }
  .focus-list li { position: relative; padding-left: 17px; margin-bottom: 12.5px; }
  .focus-list li:nth-child(3) { width: 610px; margin-bottom: 13px; }
  .focus-list li::before {
    content: ""; position: absolute; left: 2px; top: 6px;
    width: 7px; height: 7px;
    border-top: 3px solid var(--orange); border-right: 3px solid var(--orange);
    transform: rotate(45deg);
  }

  .leader-title {
    position: absolute; left: 39px; top: 517px;
    font-family: "Oswald", sans-serif; font-weight: 500; font-size: 23px;
    color: var(--orange); letter-spacing: -0.3px;
  }
  .leader-bio { position: absolute; left: 39px; top: 562px; width: 520px; font-size: 14.6px; line-height: 19.5px; }
  .leader-bio p + p { margin-top: 32px; margin-left: 3px; }

  .leader-photo {
    position: absolute; left: 572px; top: 502px; width: 220px; height: 340px;
    border: 6px solid var(--navy);
    background: linear-gradient(160deg, var(--photo-dark) 0%, var(--photo-light) 55%, var(--navy) 100%);
  }

  .guarantee {
    position: absolute; left: 0; top: 869px; width: 828px; height: 38px;
    background: var(--orange); color: var(--white);
    font-family: "Oswald", sans-serif; font-weight: 600; font-size: 23px; line-height: 38px;
    padding-left: 58px; letter-spacing: -0.3px;
  }

  .outcome { position: absolute; left: 54px; top: 937px; font-weight: 700; font-size: 17.3px; color: var(--navy); }
  .outcome-rule { position: absolute; left: 54px; top: 971px; width: 574px; height: 3px; background: var(--orange); }

  .extras-lead { position: absolute; left: 58px; top: 995px; font-size: 14.6px; }
  .extras {
    position: absolute; left: 58px; top: 1027px; width: 620px;
    display: grid; grid-template-columns: 348px 1fr; row-gap: 12px;
    list-style: none; font-size: 14.6px; line-height: 20px;
  }
  .extras li { position: relative; padding-left: 15px; }
  .extras li::before { content: ""; position: absolute; left: 2px; top: 8px; width: 5px; height: 5px; border-radius: 50%; background: var(--ink); }

  .footer {
    position: absolute; left: 0; top: 1126px; width: 828px; height: 34px;
    background: var(--navy); color: var(--white);
    display: flex; align-items: center; justify-content: center; gap: 14px;
    font-size: 16.5px; letter-spacing: 1px;
  }
  .footer-dot { width: 10px; height: 10px; border-radius: 50%; border: 2px solid var(--orange); }
</style>
</head>
<body>
  <main class="flyer">
    <section class="hero">
      <svg class="hero-shape" width="828" height="495" viewBox="0 0 828 495" aria-hidden="true">
        <path d="M0 0 H828 V450 Q414 535 0 450 Z" fill="var(--navy)"/>
      </svg>
      <h1 class="headline">Är du en kvinna som gillar att prestera, vill förbättra ditt ledarskap och leva ett själfullt liv?</h1>
      <div class="headline-rule"></div>
      <div class="intro">
        <p>Utbildningen varvar det personliga med det professionella så att du samtidigt som du ökar din arbetspres­tation även fördjupar kontakten med ditt inre, får nya perspektiv, hanterar stressen konstruktivt och skapar ett liv med god balans - både på arbetet och livet som helhet.</p>
        <p>Utbildningen består av 2 fristående moduler på 2 + 3 dagar + online uppföljning. Man kan alltså välja att göra 2 eller 5 dagar, alltefter behov. Modulerna är uppbyggda så att innehållet passar oavsett om du leder projekt, medarbetare eller större enheter :</p>
      </div>
      <ul class="focus-list">
        <li>Vi arbetar med att effektivisera arbetstiden genom analys, prioriteringar, mål och time management.</li>
        <li>Vi arbetar med kommunikation genom coaching, feedback, svåra samtal och stakeholder management.</li>
        <li>Vi arbetar med stresshantering genom avslappning, mindfulness, mental träning och tankens kraft.</li>
        <li>Vi arbetar med inre kontakt och den feminina essensen genom meditationer, samtal och övningar för ökad medvetenhet och djupare förankring i själ och hjärta.</li>
      </ul>
    </section>

    <h2 class="leader-title">Kursledaren Maria Lindqvist Berg :</h2>
    <div class="leader-bio">
      <p>Jag är en modern mystiker och ledarskapsutvecklare som de senaste 16 åren har tillhandahållit tusentals timmar med coaching, kurser och föreläsningar. Antingen har det varit ledarskapsutbildningar med fokus på prestation och leverans på t.ex. Fjällbanken, Ängsmejeriet, Kronbryggeriet, Stegsko, Tryggbo, Vindkraft Nord, Hörnbutiken m.fl. eller utbildningar med fokus på meditation och den feminina essensen. Nu är det dags att kombinera dessa områden!</p>
      <p>Med Tall Heron Ledarskap vill jag ge ett rum till just kvinnor i ledande positioner att ta sig an det arbete och de enorma möjligheter som ligger framför oss om vi fokuserar på vårt ledarskap, omvandlar stressen till kraft, låter det djupa varandet guida oss och öppnar vårt sinne för den kreativitet och struktur som behövs för att möta morgondagens utmaningar.</p>
    </div>
    <div class="leader-photo" role="img" aria-label="Porträttfoto av kursledaren med armarna i kors framför en tegelvägg"></div>

    <div class="guarantee">PENGAR-TILLBAKA-GARANTI : Om du inte är nöjd så får du 100 % tillbaka !</div>

    <h3 class="outcome">Du kommer att lämna utbildningen påfylld, inspirerad och förberedd!</h3>
    <div class="outcome-rule"></div>
    <p class="extras-lead">Dessutom får du med dig :</p>
    <ul class="extras">
      <li>Personlig handlings -och utvecklingsplan</li>
      <li>Konkreta verktyg för ledarskapet</li>
      <li>Konkreta verktyg för ditt välmående</li>
      <li>Nätverk av likasinnade kvinnor</li>
    </ul>

    <footer class="footer"><span class="footer-dot"></span><span>www.tallheron.se</span></footer>
  </main>
</body>
</html>
```